Stonebrook Business Card Redesign & Logo Update

We need to update our business cards to something more modern and fresh. Stonebrook can provide the current color schemes and old design examples, but welcome creativity in helping us with this redesign. PLEASE NOTE that we no longer utilize the "tree" and/or "leaf" imagery in our branding. If able would apprecaite an update on the quality of our "words only" logo in Ai. / PNG formats too.

Target Market(s)

Investors, landowners, corporate partners, contractors

Industry/Entity Type

Environmental Restoration & Conservation

Contact Information for Business Card

Logo, persons name, title, mailing address, phone and email, website url

Font styles to use
Other font styles liked:
• Merriweather

Requirements
Nice to have
• Logo, persons name, title, mailing address, phone and email, website url, but open to ideams
Should not have
• No all back backgrounds

```html
<!DOCTYPE html>
<html lang="en">
<head>
<meta charset="utf-8">
<title>Stonebrook Business Cards</title>
<link href="https://fonts.googleapis.com/css2?family=Merriweather:wght@400;700;900&display=swap" rel="stylesheet">
<style>
  :root {
    --orange: #ee7d22;
    --green: #157a3b;
    --ink: #1e1e1e;
    --card: #ffffff;
    --backdrop: #e6e6e6;
  }
  * { box-sizing: border-box; margin: 0; padding: 0; }
  html, body {
    width: 1200px; height: 1059px; overflow: hidden;
    background: var(--backdrop);
    font-family: "Merriweather", Georgia, serif;
    color: var(--ink);
  }
  .sheet { position: relative; width: 1200px; height: 1059px; }
  .card {
    position: absolute; left: 190px;
    width: 820px; height: 468px;
    background: var(--card);
    box-shadow: 0 10px 30px rgba(0,0,0,.18);
    overflow: hidden;
  }
  .card--front { top: 44px; }
  .card--back { top: 547px; }

  .wordmark {
    font-family: "Merriweather", Georgia, serif;
    font-weight: 900;
    color: var(--green);
    letter-spacing: 2px;
    text-transform: uppercase;
    line-height: 1;
  }
  .card--front .wordmark {
    position: absolute; left: 0; right: 0; top: 200px;
    text-align: center; font-size: 64px;
  }
  .card--back .wordmark {
    position: absolute; right: 48px; top: 48px;
    font-size: 34px;
  }

  .person { position: absolute; left: 52px; top: 178px; }
  .person__name {
    font-weight: 900; font-size: 27px; letter-spacing: 1px;
    text-transform: uppercase;
  }
  .person__first { color: var(--orange); }
  .person__last { color: var(--green); }
  .person__title { font-size: 20px; margin-top: 4px; }

  .contacts { position: absolute; left: 52px; top: 318px; list-style: none; }
  .contacts li {
    display: flex; align-items: center; gap: 12px;
    font-size: 21px; line-height: 32px;
  }
  .contacts svg { width: 18px; height: 18px; flex: none; }

  .address {
    position: absolute; right: 48px; top: 196px;
    text-align: right; font-size: 19px; line-height: 30px;
    font-style: normal;
  }

  .band { position: absolute; left: 0; bottom: 0; width: 820px; height: 86px; }
</style>
</head>
<body>
<main class="sheet">
  <section class="card card--front" aria-label="Card front">
    <div class="wordmark">Stonebrook</div>
  </section>

  <section class="card card--back" aria-label="Card back">
    <div class="wordmark">Stonebrook</div>

    <div class="person">
      <p class="person__name"><span class="person__first">Martin</span> <span class="person__last">Hale</span></p>
      <p class="person__title">Founder</p>
    </div>

    <address class="address">
      Stonebrook Office<br>
      18 Ridgeline Rd, PO Box 2716
    </address>

    <ul class="contacts">
      <li>
        <svg viewBox="0 0 20 20" aria-hidden="true"><path fill="var(--orange)" d="M5 2l3 4-2 2c1 2 3 4 5 5l2-2 4 3-2 3C9 17 3 11 2 5z"/></svg>
        (555) 214-3090
      </li>
      <li>
        <svg viewBox="0 0 20 20" aria-hidden="true"><rect x="2" y="4" width="16" height="12" fill="var(--orange)"/><path d="M2 4l8 7 8-7" fill="none" stroke="#fff" stroke-width="1.6"/></svg>
        hello@stonebrookcredit.com
      </li>
      <li>
        <svg viewBox="0 0 20 20" aria-hidden="true"><circle cx="10" cy="10" r="8" fill="var(--orange)"/><path d="M2 10h16M10 2c-4 5-4 11 0 16M10 2c4 5 4 11 0 16" fill="none" stroke="#fff" stroke-width="1.2"/></svg>
        www.stonebrookcredit.com
      </li>
    </ul>

    <svg class="band" viewBox="0 0 820 86" preserveAspectRatio="none" aria-hidden="true">
      <rect x="0" y="66" width="820" height="20" fill="var(--orange)"/>
      <polygon points="330,86 420,30 560,30 560,86" fill="var(--orange)"/>
      <rect x="560" y="30" width="150" height="56" fill="var(--green)"/>
      <polygon points="716,86 724,30 820,30 820,86" fill="var(--orange)"/>
    </svg>
  </section>
</main>
</body>
</html>
```